New Law Firm needs a business card design

I need a business card for my new law firm called Tansey Wills and Probate. I would like designs to use my logo attached. My firm is new and modern. I like the colors orange, white, grey and black. The design I will chose will be one which uses color well, one which looks impressive, smart and modern.

Target Market(s)

Adults aged 30 to 50 seeking professional advice.

Industry/Entity Type

Law Firm

Requirements
Must have
• My logo which is attached.

Must have a modern font, similar to my logo and draft business card.
Should not have
• Any symbols about law, such as scales etc.

```html
<!DOCTYPE html>
<html lang="en">
<head>
<meta charset="utf-8">
<title>Tansey Wills and Probate – Business Card</title>
<link href="https://fonts.googleapis.com/css2?family=Questrial&display=swap" rel="stylesheet">
<style>
  :root {
    --page: #efeeec;
    --card: #ffffff;
    --orange: #f5a04a;
    --grey: #8a8a8a;
    --grey-dark: #555555;
    --ink: #2b2b2b;
  }
  * { margin: 0; padding: 0; box-sizing: border-box; }
  html, body { width: 1200px; height: 1000px; overflow: hidden; }
  body {
    background: var(--page);
    font-family: "Questrial", sans-serif;
    position: relative;
  }
  .card {
    position: absolute;
    width: 560px;
    height: 320px;
    background: var(--card);
    box-shadow: 0 4px 14px rgba(0,0,0,0.18);
  }
  .card--back { left: 70px; top: 150px; }
  .card--front { left: 570px; top: 530px; }

  .rule {
    position: absolute;
    left: 0; right: 0;
    height: 2px;
    background: var(--orange);
  }
  .card--back .rule { bottom: 34px; }
  .card--front .rule { bottom: 58px; }

  .brand {
    position: absolute;
    color: var(--grey-dark);
    font-size: 16px;
    letter-spacing: 1px;
    line-height: 1.3;
  }
  .card--back .brand { left: 30px; bottom: 52px; text-align: left; }
  .card--front .brand { right: 36px; top: 60px; text-align: right; font-size: 19px; }

  .contact {
    position: absolute;
    right: 30px;
    top: 36px;
    list-style: none;
    color: var(--grey);
    font-size: 17px;
  }
  .contact__item {
    display: flex;
    justify-content: flex-end;
    align-items: center;
    gap: 14px;
    height: 26px;
  }
  .contact__item--email { margin-top: 14px; }
  .contact__icon { width: 22px; height: 18px; flex: none; }

  .person {
    position: absolute;
    left: 30px;
    bottom: 70px;
  }
  .person__name {
    font-size: 27px;
    color: var(--ink);
    font-weight: 400;
  }
  .person__role {
    font-size: 17px;
    color: var(--grey-dark);
    margin-left: 6px;
  }
  .person__quals {
    font-size: 16px;
    color: var(--orange);
    margin-top: 2px;
  }
</style>
</head>
<body>

<section class="card card--back" aria-label="Card back">
  <ul class="contact">
    <li class="contact__item">Address: To be confirmed
      <svg class="contact__icon" viewBox="0 0 22 18" aria-hidden="true"><rect x="1" y="2" width="20" height="14" fill="none" stroke="#222" stroke-width="1.5"/><path d="M1 2 L11 10 L21 2" fill="none" stroke="#222" stroke-width="1.5"/></svg>
    </li>
    <li class="contact__item">Phone: To be confirmed
      <svg class="contact__icon" viewBox="0 0 22 18" aria-hidden="true"><rect x="7" y="0" width="9" height="18" rx="1.5" fill="#222"/><rect x="8.5" y="2" width="6" height="11" fill="#fff"/></svg>
    </li>
    <li class="contact__item">Fax: To be confirmed
      <svg class="contact__icon" viewBox="0 0 22 18" aria-hidden="true"><rect x="5" y="0.5" width="12" height="7" fill="none" stroke="#222" stroke-width="1.2"/><rect x="1" y="7" width="20" height="10.5" rx="1.5" fill="none" stroke="#222" stroke-width="1.5"/><path d="M6 11 q5 -3 10 0" fill="none" stroke="#222" stroke-width="2"/></svg>
    </li>
    <li class="contact__item contact__item--email">Email: daniel@tanseyprobate.com.au
      <svg class="contact__icon" viewBox="0 0 22 18" aria-hidden="true"><rect x="1" y="2" width="20" height="14" fill="none" stroke="#222" stroke-width="1.5"/><path d="M1 2 L21 16 M21 2 L1 16" fill="none" stroke="#222" stroke-width="1.5"/></svg>
    </li>
  </ul>

  <p class="brand">Tansey<br>Wills &amp; Probate</p>
  <div class="rule"></div>
</section>

<section class="card card--front" aria-label="Card front">
  <p class="brand">Tansey<br>Wills &amp; Probate</p>

  <div class="person">
    <p><span class="person__name">Daniel Marsh</span><span class="person__role">Lawyer</span></p>
    <p class="person__quals">Assoc.Deg.Law, BLJSt, LLB, Grad Dip Law.</p>
  </div>
  <div class="rule"></div>
</section>

</body>
</html>
```